Process Roadmap for Interior Design Firm

We are looking to ramp up the design appeal of our current process roadmap to be very visually interesting, while staying informative and descriptive about our process.

Target Market(s)

In-house Clients

Industry/Entity Type

Interior Design Firm focused on sustainable and holistic design.

Other font styles liked:
• raleway

Requirements
Must have
• 1.) it would be nice if the graphic provided a more clear indication of the “journey” from one step to the next, so that there was a clear sense of the progression (such that we are directing the viewer) 2.). We would want it to fit on an 8.5”x11” page (the page could be horizontal when we have the Calm Compass formatted out with the testimonials) (in addition to the testimonials, we may also want to have the detailed descriptions of each step of the process presented below the graphic, so that the graphic is cleaner) 3.) ideally the graphic is clear and simple enough to also be used on our Bi-Weekly Client Updates, which will be typed updates for clients re their project budgets, schedule and scope. The Calm Compass graphic (without all the testimonials) would be at the end of the update, and would fit on the page horizontally at the bottom, perhaps in a space which is 7.5”w x 4”h or so.
Should not have
• bold or bright colors. Natural neutrals are preferred, such as the ones featured on the provided graphic.

```html
<!DOCTYPE html>
<html lang="en">
<head>
<meta charset="utf-8">
<title>ALD Calm Compass</title>
<link rel="stylesheet" href="https://fonts.googleapis.com/css2?family=Raleway:ital,wght@0,300;0,400;0,700;0,800;1,500&display=swap">
<style>
  :root {
    --backdrop: #f1f1f1;
    --page: #ffffff;
    --band: #e2dbd1;
    --gold: #c5b89e;
    --gold-deep: #bfae87;
    --title: #777777;
    --heading: #666666;
    --body: #9a9a9a;
    --card-text: #7a7a7a;
    --path: #efefef;
    --hex-top: #f3ead8;
    --hex-left: #7e7762;
    --hex-right: #bcae88;
    --avatar: #9b9b9b;
    --quote: #f0ede6;
  }
  * { margin: 0; padding: 0; box-sizing: border-box; }
  html, body { width: 1200px; height: 984px; overflow: hidden; }
  body {
    background: var(--backdrop);
    font-family: "Raleway", sans-serif;
    position: relative;
  }
  .page {
    position: absolute;
    left: 102px; top: 107px;
    width: 996px; height: 770px;
    background: var(--page);
  }
  .page__band {
    position: absolute; left: 0; top: 0;
    width: 100%; height: 15px;
    background: var(--band);
  }
  .brand {
    position: absolute; left: 56px; top: 44px;
    width: 94px; height: 45px;
    background: var(--gold);
    display: flex; align-items: center; gap: 6px;
    padding-left: 8px;
  }
  .brand__mark { width: 10px; height: 10px; background: var(--page); opacity: .85; }
  .brand__name {
    color: var(--page);
    font-size: 8px; font-weight: 400;
    letter-spacing: 1px; line-height: 1.25;
    text-transform: uppercase;
  }
  .page__title {
    position: absolute; left: 56px; top: 106px;
    font-size: 38px; font-weight: 800;
    color: var(--title); letter-spacing: -0.5px;
  }
  .roadmap { position: absolute; left: 0; top: 0; }
  .step-number {
    font-family: "Raleway", sans-serif;
    font-style: italic; font-weight: 500;
    font-size: 20px; fill: var(--gold-deep);
    letter-spacing: 3px;
  }
  .step {
    position: absolute; width: 110px;
  }
  .step--high { top: 285px; }
  .step--low { top: 369px; }
  .step__title {
    font-size: 16px; font-weight: 700; color: var(--heading);
  }
  .step__rule {
    width: 21px; height: 2px; background: var(--gold);
    margin: 6px 0 8px;
  }
  .step__text {
    font-size: 11.2px; font-weight: 300; color: var(--body);
    line-height: 13.6px;
  }
  .testimonials__title {
    position: absolute; left: 0; width: 100%; top: 566px;
    text-align: center;
    font-size: 25px; font-weight: 800; color: var(--title);
  }
  .testimonial {
    position: absolute; top: 601px;
    width: 198px; height: 120px;
    background: var(--page);
    box-shadow: 0 2px 14px rgba(0,0,0,.07);
    text-align: center;
  }
  .testimonial__quote {
    position: absolute; left: 8px; top: 2px;
    font-size: 56px; font-weight: 800; font-style: italic;
    color: var(--quote); line-height: 1;
  }
  .testimonial__avatar {
    width: 37px; height: 37px; border-radius: 50%;
    background: var(--avatar);
    margin: 7px auto 0;
  }
  .testimonial__stars {
    color: var(--gold-deep); font-size: 10px; letter-spacing: 1px;
    margin-top: 3px;
  }
  .testimonial__text {
    font-size: 10.4px; font-weight: 400; color: var(--card-text);
    line-height: 12.3px; margin: 9px 14px 0;
  }
</style>
</head>
<body>
  <main class="page">
    <div class="page__band"></div>

    <div class="brand">
      <span class="brand__mark"></span>
      <span class="brand__name">Ashwell Lane<br>Design</span>
    </div>

    <h1 class="page__title">ALD CALM COMPASS</h1>

    <svg class="roadmap" width="996" height="560" viewBox="0 0 996 560" aria-hidden="false">
      <defs>
        <g id="hex-block">
          <polygon points="-44,-6 -22,13 -22,26 -44,7" fill="var(--hex-left)"/>
          <polygon points="-22,13 18,17 44,-3 44,10 18,30 -22,26" fill="var(--hex-right)"/>
          <polygon points="-44,-6 -18,-27 22,-22 44,-3 18,17 -22,13" fill="var(--hex-top)"/>
        </g>
      </defs>
      <polyline points="107,218 232,300 357,218 482,300 608,218 734,300 859,218"
                fill="none" stroke="var(--path)" stroke-width="8" stroke-linejoin="round"/>

      <g transform="translate(107,213)"><use href="#hex-block"/><rect x="-14" y="-16" width="28" height="20" rx="3" fill="#e6d8bb" role="img" aria-label="Listening icon: person with headset"/></g>
      <g transform="translate(232,295)"><use href="#hex-block"/><rect x="-14" y="-16" width="28" height="20" rx="3" fill="#e6d8bb" role="img" aria-label="Visioning icon: hand holding a target"/></g>
      <g transform="translate(357,213)"><use href="#hex-block"/><rect x="-14" y="-16" width="28" height="20" rx="3" fill="#e6d8bb" role="img" aria-label="Planning icon: board with charts"/></g>
      <g transform="translate(482,295)"><use href="#hex-block"/><rect x="-14" y="-16" width="28" height="20" rx="3" fill="#e6d8bb" role="img" aria-label="Designing icon: ruler and pencil"/></g>
      <g transform="translate(608,213)"><use href="#hex-block"/><rect x="-14" y="-16" width="28" height="20" rx="3" fill="#e6d8bb" role="img" aria-label="Managing icon: gears"/></g>
      <g transform="translate(734,295)"><use href="#hex-block"/><rect x="-14" y="-16" width="28" height="20" rx="3" fill="#e6d8bb" role="img" aria-label="Installing icon: wrench and screwdriver"/></g>
      <g transform="translate(859,213)"><use href="#hex-block"/><rect x="-14" y="-16" width="28" height="20" rx="3" fill="#e6d8bb" role="img" aria-label="Completing icon: checklist"/></g>

      <text class="step-number" x="72" y="189">01</text>
      <text class="step-number" x="197" y="271">02</text>
      <text class="step-number" x="322" y="189">03</text>
      <text class="step-number" x="447" y="271">04</text>
      <text class="step-number" x="573" y="189">05</text>
      <text class="step-number" x="699" y="271">06</text>
      <text class="step-number" x="824" y="189">07</text>
    </svg>

    <section class="step step--high" style="left:60px">
      <h2 class="step__title">Listening</h2>
      <div class="step__rule"></div>
      <p class="step__text">Listening to our clients, their land, and their home. Identifying their needs, challenges, wishes, and dreams.</p>
    </section>
    <section class="step step--low" style="left:188px">
      <h2 class="step__title">Visioning</h2>
      <div class="step__rule"></div>
      <p class="step__text">Facilitating a guided visioning process to clarify the deepest intention, true purpose, and highest potential for their home and their future within it.</p>
    </section>
    <section class="step step--high" style="left:316px">
      <h2 class="step__title">Planning</h2>
      <div class="step__rule"></div>
      <p class="step__text">Turning our client's vision into a clearly defined scope, budget, and timeline. Mapping out the steps for making their dream a reality. Setting a meeting schedule from start to finish.</p>
    </section>
    <section class="step step--low" style="left:444px">
      <h2 class="step__title">Designing</h2>
      <div class="step__rule"></div>
      <p class="step__text">Following the schedule through the design phases from initial design concepts, technical drawings and design is executed with details, and the selection of all finishes, fixtures, and furnishings.</p>
    </section>
    <section class="step step--high" style="left:571px">
      <h2 class="step__title">Managing</h2>
      <div class="step__rule"></div>
      <p class="step__text">Listening to our clients, their land, and their home. Identifying their needs, challenges, wishes, and dreams. excellence, and the construction and furnishings are on-time and on-budget.</p>
    </section>
    <section class="step step--low" style="left:699px">
      <h2 class="step__title">Installing</h2>
      <div class="step__rule"></div>
      <p class="step__text">Overseeing the inspection, installation, and arrangement of all furnishings, lighting, artwork, and decorative items. Taking care of every last detail</p>
    </section>
    <section class="step step--high" style="left:827px">
      <h2 class="step__title">Completing</h2>
      <div class="step__rule"></div>
      <p class="step__text">Fixing any issues or defects. Follow up on all remaining items. Completing the final finishing touches to our client's full and total satisfaction.</p>
    </section>

    <h2 class="testimonials__title">TESTIMONIALS</h2>

    <article class="testimonial" style="left:71px">
      <span class="testimonial__quote">&ldquo;</span>
      <div class="testimonial__avatar" role="img" aria-label="Client portrait"></div>
      <div class="testimonial__stars">★★★★★</div>
      <p class="testimonial__text">Ava to send over testimonials for fill this space-three or four columns of testimonials</p>
    </article>
    <article class="testimonial" style="left:301px">
      <span class="testimonial__quote">&ldquo;</span>
      <div class="testimonial__avatar" role="img" aria-label="Client portrait"></div>
      <div class="testimonial__stars">★★★★★</div>
      <p class="testimonial__text">Ava to send over testimonials for fill this space-three or four columns of testimonials</p>
    </article>
    <article class="testimonial" style="left:530px">
      <span class="testimonial__quote">&ldquo;</span>
      <div class="testimonial__avatar" role="img" aria-label="Client portrait"></div>
      <div class="testimonial__stars">★★★★★</div>
      <p class="testimonial__text">Ava to send over testimonials for fill this space-three or four columns of testimonials</p>
    </article>
    <article class="testimonial" style="left:760px">
      <span class="testimonial__quote">&ldquo;</span>
      <div class="testimonial__avatar" role="img" aria-label="Client portrait"></div>
      <div class="testimonial__stars">★★★★★</div>
      <p class="testimonial__text">Ava to send over testimonials for fill this space-three or four columns of testimonials</p>
    </article>
  </main>
</body>
</html>
```